Business Card and Stationary for KVT Builders
Need standard business card, letterhead, and envelopes to incorporate our new logo
Business Card and Stationary for KVT Builders - Construction
Creative Brief
Simple
Rowan Pelley
Vice President
4621 Brantwell Houston, TX 77031
rowan@kvtbuilders.example
I'm open to layout ideas for all designs. letterhead and envelopes need to be accessible to incorporate microsoft office products.

```html
<!DOCTYPE html>
<html lang="en">
<head>
<meta charset="utf-8">
<title>KVT Builders — Business Card</title>
<link href="https://fonts.googleapis.com/css2?family=Arimo:wght@400;700&display=swap" rel="stylesheet">
<style>
  :root {
    --brand-blue: #3b3ca8;
    --ink: #2c2c6e;
    --tagline-light: #ececf4;
    --white: #ffffff;
    --page: #ffffff;
    --card-edge: #e4e4ea;
  }
  * { box-sizing: border-box; margin: 0; padding: 0; }
  html, body {
    width: 1200px; height: 341px; overflow: hidden;
    background: var(--page);
    font-family: "Arimo", Arial, sans-serif;
  }
  .sheet { position: relative; width: 1200px; height: 341px; }
  .card {
    position: absolute; top: 0; width: 588px; height: 341px; overflow: hidden;
  }
  .card--front { left: 4px; background: var(--white); border: 1px solid var(--card-edge); }
  .card--back { left: 608px; background: var(--brand-blue); }
  .card__wave { position: absolute; left: 0; bottom: 0; width: 100%; height: 100%; }

  .brand { position: absolute; display: flex; flex-direction: column; align-items: center; }
  .brand__row { display: flex; align-items: center; gap: 8px; }
  .brand__mark { width: 16px; height: 16px; background: currentColor; }
  .brand__name { font-weight: 700; line-height: 1; }
  .brand__tagline { font-weight: 700; line-height: 1; margin-top: 6px; }

  .card--front .brand { left: 40px; top: 100px; width: 250px; color: var(--brand-blue); }
  .card--front .brand__name { font-size: 34px; }
  .card--front .brand__tagline { font-size: 13.5px; }

  .divider {
    position: absolute; left: 312px; top: 56px; width: 2px; height: 132px;
    background: var(--brand-blue);
  }
  .contact {
    position: absolute; left: 330px; top: 62px;
    color: var(--ink); font-size: 12.5px; line-height: 1.3; font-style: normal;
  }
  .contact__name { font-size: 15px; color: var(--brand-blue); }
  .contact__title { margin-bottom: 10px; }

  .card--back .brand { left: 0; right: 0; top: 124px; color: var(--white); }
  .card--back .brand__name { font-size: 42px; }
  .card--back .brand__tagline { font-size: 16px; color: var(--tagline-light); }
</style>
</head>
<body>
<main class="sheet">
  <section class="card card--front" aria-label="Business card front">
    <svg class="card__wave" viewBox="0 0 588 341" preserveAspectRatio="none" aria-hidden="true">
      <defs>
        <linearGradient id="greyBand" x1="0" x2="1">
          <stop offset="0" stop-color="#ffffff"/>
          <stop offset="0.5" stop-color="#8d8d96"/>
          <stop offset="1" stop-color="#d8d8de"/>
        </linearGradient>
      </defs>
      <path d="M0,246 C170,308 360,262 588,228 L588,341 L0,341 Z" fill="url(#greyBand)"/>
      <path d="M0,268 C180,322 380,272 588,242 L588,341 L0,341 Z" fill="#ffffff"/>
      <path d="M0,292 C190,332 390,286 588,254 L588,341 L0,341 Z" fill="var(--brand-blue)"/>
    </svg>
    <div class="brand">
      <div class="brand__row"><span class="brand__mark"></span><span class="brand__name">KVT Builders</span></div>
      <span class="brand__tagline">Commercial Concrete Contractors</span>
    </div>
    <div class="divider"></div>
    <address class="contact">
      <div class="contact__name">Rowan Pelley</div>
      <div class="contact__title">Vice President</div>
      <div>4621 Brantwell</div>
      <div>Houston, TX 77031</div>
      <div>Phone : (713) 555-0142</div>
      <div>Cell : (713) 555-0187</div>
      <div>Fax : (713) 555-0163</div>
      <div>Email : rowan@kvtbuilders.example</div>
    </address>
  </section>

  <section class="card card--back" aria-label="Business card back">
    <svg class="card__wave" viewBox="0 0 588 341" preserveAspectRatio="none" aria-hidden="true">
      <defs>
        <linearGradient id="greyBandBack" x1="0" x2="1">
          <stop offset="0" stop-color="#3b3ca8"/>
          <stop offset="0.35" stop-color="#c8c8d0"/>
          <stop offset="0.7" stop-color="#8d8d96"/>
          <stop offset="1" stop-color="#e2e2e8"/>
        </linearGradient>
      </defs>
      <path d="M0,268 C170,318 360,270 588,214 L588,236 C370,292 180,334 0,292 Z" fill="url(#greyBandBack)"/>
      <path d="M0,300 C190,336 380,290 588,248 L588,256 C380,300 190,344 0,308 Z" fill="#b9b9c2" opacity="0.7"/>
    </svg>
    <div class="brand">
      <div class="brand__row"><span class="brand__mark"></span><span class="brand__name">KVT Builders</span></div>
      <span class="brand__tagline">Commercial Concrete Contractors</span>
    </div>
  </section>
</main>
</body>
</html>
```